Tamworth Logistics

Create a modern, simple, Elegant business card design for my business.

Services: Vexa Trucks, Transport, Contract Logistics,

Business

Include all details same as old card plus new website address: www.tamworthlogistics-demo.com.au

• Similar colors to Logo.

```html
<!DOCTYPE html>
<html lang="en">
<head>
<meta charset="utf-8">
<title>Tamworth Logistics – Business Card</title>
<link href="https://fonts.googleapis.com/css2?family=Roboto:wght@400;500;700&display=swap" rel="stylesheet">
<style>
  :root {
    --page-bg: #e4e4e4;
    --blue-deep: #0b5a8a;
    --blue-mid: #136ea3;
    --blue-light: #1a88bd;
    --accent-blue: #5ab0e3;
    --card-black: #1f1f20;
    --edge-black: #0c0c0c;
    --silver: #9a9a9a;
    --text-light: #e9e9e9;
    --white: #ffffff;
  }
  * { box-sizing: border-box; margin: 0; padding: 0; }
  html, body { width: 1200px; height: 576px; overflow: hidden; }
  body {
    background: var(--page-bg);
    font-family: "Roboto", Arial, sans-serif;
    position: relative;
  }
  .card {
    position: absolute;
    top: 138px;
    border-radius: 12px;
    overflow: hidden;
    box-shadow: 0 2px 6px rgba(0,0,0,0.25);
  }

  /* Front */
  .card-front {
    left: 82px;
    width: 484px;
    height: 294px;
    background: var(--edge-black);
  }
  .front-face {
    position: absolute;
    inset: 0 0 7px 0;
    border-radius: 12px 12px 10px 10px;
    background: linear-gradient(180deg, var(--blue-deep) 0%, var(--blue-mid) 55%, var(--blue-light) 100%);
  }
  .front-photo {
    position: absolute;
    left: 120px; top: 40px;
    width: 260px; height: 160px;
    background: radial-gradient(ellipse at center, rgba(150,190,215,0.25) 0%, rgba(150,190,215,0) 70%);
  }
  .front-wordmark {
    position: absolute;
    top: 112px; left: 0; right: 0;
    text-align: center;
    color: var(--white);
    font-weight: 700;
    font-size: 34px;
    letter-spacing: 0.5px;
  }
  .front-services {
    position: absolute;
    top: 250px; left: 0; right: 0;
    display: flex;
    justify-content: center;
    gap: 15px;
    color: #d6e8f3;
    font-size: 11.5px;
    text-transform: uppercase;
  }

  /* Back */
  .card-back {
    left: 602px;
    width: 480px;
    height: 292px;
    background: var(--card-black);
  }
  .back-wordmark {
    position: absolute;
    left: 16px; top: 46px;
    color: #c9c9c9;
    font-weight: 700;
    font-size: 26px;
  }
  .holder {
    position: absolute;
    right: 24px; top: 132px;
    text-align: right;
  }
  .holder-name {
    color: var(--accent-blue);
    font-weight: 500;
    font-size: 20px;
    line-height: 1;
  }
  .holder-role {
    color: var(--text-light);
    font-size: 11.5px;
    margin-top: 7px;
  }
  .divider {
    position: absolute;
    left: 25px; top: 170px;
    width: 326px; height: 1px;
    background: var(--accent-blue);
  }
  .contacts {
    position: absolute;
    left: 28px; top: 190px;
    list-style: none;
    color: var(--text-light);
    font-size: 12.5px;
  }
  .contacts li { display: flex; align-items: center; height: 17px; }
  .contacts svg { width: 11px; height: 11px; margin-right: 12px; fill: var(--accent-blue); }
  .services {
    position: absolute;
    right: 24px; top: 190px;
    list-style: none;
    text-align: right;
    color: var(--text-light);
    font-size: 12.5px;
  }
  .services li { height: 17px; line-height: 17px; }
  .services .mark { color: var(--accent-blue); margin-left: 4px; }
  .back-bands { position: absolute; left: 0; bottom: 0; width: 480px; height: 36px; }
</style>
</head>
<body>
  <section class="card card-front">
    <div class="front-face">
      <div class="front-photo" role="img" aria-label="Faded photo of a truck on the road"></div>
      <div class="front-wordmark">Tamworth Logistics</div>
      <div class="front-services">
        <span>Vexa Trucks</span><span>Transport</span><span>Contract Logistics</span><span>Hotshots</span>
      </div>
    </div>
  </section>

  <section class="card card-back">
    <div class="back-wordmark">Tamworth Logistics</div>
    <div class="holder">
      <div class="holder-name">Liam Carter</div>
      <div class="holder-role">Managing Director</div>
    </div>
    <div class="divider"></div>
    <ul class="contacts">
      <li><svg viewBox="0 0 12 12"><path d="M1 4c0-2 2-3 5-3s5 1 5 3l-2 1-1-1.5H4L3 5zM2.5 6h7l1 5h-9z"/></svg>0400 555 182</li>
      <li><svg viewBox="0 0 12 12"><circle cx="6" cy="6" r="5" fill="none" stroke="#5ab0e3" stroke-width="1.2"/><path d="M1 6h10M6 1c-2.5 3-2.5 7 0 10M6 1c2.5 3 2.5 7 0 10" fill="none" stroke="#5ab0e3" stroke-width="1"/></svg>www.tamworthlogistics-demo.com.au</li>
      <li><svg viewBox="0 0 12 12"><path d="M1 2.5h10v7H1z"/><path d="M1 2.5l5 4 5-4" fill="none" stroke="#1f1f20" stroke-width="1"/></svg>info@tamworthlogistics-demo.com.au</li>
    </ul>
    <ul class="services">
      <li>Vexa Trucks<span class="mark">«</span></li>
      <li>Contract Logistics<span class="mark">«</span></li>
      <li>Hotshots<span class="mark">«</span> Transport<span class="mark">«</span></li>
    </ul>
    <svg class="back-bands" viewBox="0 0 480 36" aria-hidden="true">
      <defs>
        <linearGradient id="bandBlue" x1="0" y1="0" x2="0" y2="1">
          <stop offset="0" stop-color="#1a7fb8"/><stop offset="1" stop-color="#0b5a8a"/>
        </linearGradient>
      </defs>
      <polygon points="0,18 270,18 260,36 0,36" fill="#9a9a9a"/>
      <polygon points="270,0 480,0 480,36 254,36" fill="url(#bandBlue)"/>
    </svg>
  </section>
</body>
</html>
```